Talvok Engineering Business card Design

We need to make business cards for our NDT and inspection company. The company is called Talvok Engineering. We want a professional modern feel business card. We have just completed the remaking of our website and would like to have business cards with the same feel and colours. The final design should communicate professionalism and cutting edge tech.

Target Market(s)

We sell to B2B Business clients. Our customer is an engineer or decision maker in the mechanical engineering / Oil and gas field.

Contact Information for Business Card

Please see the current business cards that we have uploaded to get the details. You can also look at our Website www.talvok-eng.example for more.

Requirements
Must have
• Less is more
Nice to have
• Less is more

```html
<!DOCTYPE html>
<html lang="en">
<head>
<meta charset="utf-8">
<title>Talvok Engineering – Business Card</title>
<link rel="stylesheet" href="https://fonts.googleapis.com/css2?family=Montserrat:wght@600;700&family=Open+Sans:wght@400;600&display=swap">
<style>
  :root {
    --stage: #3b3b3d;
    --navy: #1f3578;
    --navy-deep: #18295f;
    --red: #b0141c;
    --white: #ffffff;
    --muted: #c9d2ea;
  }
  * { box-sizing: border-box; margin: 0; padding: 0; }
  html, body {
    width: 1200px; height: 900px; overflow: hidden;
    background: var(--stage);
    font-family: "Open Sans", Arial, sans-serif;
  }
  .card {
    position: absolute;
    left: 285px;
    width: 630px; height: 360px;
    border-radius: 22px;
    overflow: hidden;
    background: linear-gradient(135deg, var(--navy) 0%, var(--navy-deep) 100%);
    color: var(--white);
    box-shadow: 0 14px 30px rgba(0,0,0,.45);
  }
  .card--front { top: 60px; }
  .card--back  { top: 480px; }

  /* front */
  .front-emblem { position: absolute; inset: 0; width: 100%; height: 100%; }
  .identity { position: absolute; left: 44px; top: 48px; }
  .identity__name {
    font-family: "Montserrat", Arial, sans-serif;
    font-weight: 700; font-size: 28px; letter-spacing: 1.5px;
    text-transform: uppercase;
  }
  .identity__role { font-size: 15px; color: var(--muted); margin-top: 2px; }
  .contact { position: absolute; left: 44px; top: 160px; list-style: none; font-size: 15px; line-height: 1.5; }
  .contact__address { margin-bottom: 6px; }
  .contact__item { display: flex; align-items: center; gap: 8px; }
  .contact__icon { width: 11px; height: 11px; flex: none; fill: var(--white); }
  .brand-name {
    position: absolute; left: 360px; top: 162px; width: 250px;
    text-align: center;
    font-family: "Montserrat", Arial, sans-serif;
    font-weight: 700; font-size: 25px; line-height: 1.2;
    color: var(--navy);
  }

  /* back */
  .services { position: absolute; list-style: none; font-size: 15px; line-height: 1.45; font-weight: 600; }
  .services--primary { left: 48px; top: 40px; }
  .services--secondary { left: 330px; top: 180px; }
  .services li { display: flex; align-items: center; gap: 10px; }
  .services li::before {
    content: ""; width: 8px; height: 8px; border-radius: 50%;
    background: var(--white); flex: none;
  }
</style>
</head>
<body>

<section class="card card--front" aria-label="Card front">
  <svg class="front-emblem" viewBox="0 0 630 360" aria-hidden="true">
    <path d="M292 300 A200 200 0 0 1 500 -10" fill="none" stroke="var(--red)" stroke-width="9" stroke-linecap="round"/>
    <circle cx="488" cy="190" r="200" fill="var(--white)"/>
  </svg>

  <div class="identity">
    <h1 class="identity__name">Dorian Halvek</h1>
    <p class="identity__role">Director</p>
  </div>

  <ul class="contact">
    <li class="contact__address">2215 Ferncliff Avenue<br>Marlow, 40517</li>
    <li class="contact__item">
      <svg class="contact__icon" viewBox="0 0 12 12"><path d="M2.5 0.5l2 2.5-1.2 1.3c.7 1.6 2 2.9 3.5 3.6L8 6.6l2.5 2-1 2.6C5 11 1 7 .8 2.4z"/></svg>
      +330 5512-0934
    </li>
    <li class="contact__item">
      <svg class="contact__icon" viewBox="0 0 12 12"><path d="M0 2h12v8H0z M1 3l5 3.5L11 3v-.2H1z" fill-rule="evenodd"/></svg>
      info@talvok-eng.example
    </li>
    <li class="contact__item">
      <svg class="contact__icon" viewBox="0 0 12 12"><circle cx="6" cy="6" r="5" fill="none" stroke="var(--white)" stroke-width="1.6"/><circle cx="6" cy="6" r="1.8"/></svg>
      www.talvok-eng.example
    </li>
  </ul>

  <p class="brand-name">Talvok Engineering</p>
</section>

<section class="card card--back" aria-label="Card back">
  <ul class="services services--primary">
    <li>API 653 Tank Inspections</li>
    <li>API 570 Pipeline Inspections</li>
    <li>API 510 Pressure Vessel Inspections</li>
    <li>Welding Inspection</li>
    <li>Electrical Inspection</li>
    <li>OCTG Inspections</li>
  </ul>
  <ul class="services services--secondary">
    <li>Lifting Equipment Inspections</li>
    <li>Non-Destructive Testing</li>
    <li>UT / PT / MT / RT / VT</li>
    <li>Advanced NDT</li>
    <li>PAUT / MFL / ILI</li>
    <li>Engineering Projects</li>
  </ul>
</section>

</body>
</html>
```